Postcard Design

We are an upscale, full service real estate boutique based in Mt. Pleasant, SC. We will be having a Grand Opening of our beautiful, new office complete with high end custom home architecture and design. I will attach photos for your review. I would like to come up with a medium postcard to be mailed to clientele of Mt. Pleasant. Home prices between $300,000 - $2.2 million. The customers can call our office for the Grand Opening Listing Promotion or stop by our grand opening. We will have drawings for door prizes that include services at Brindlecove Day Spa, Copper Kettle Pies gift certificates, and they can register to win a cruise with a listing presentation. Our Grand Opening will be a couple of different dates, April 7, 2016 and April 21, 2016. I will want an order that lists the 7th and another order that will list the 21. The look should have a very "relaxing, beach" feel, but not Myrtle Beach...should reflect colors of the ocean, like you are on vacation. I will include logos and pics for your review. Thank you!

```html
<!DOCTYPE html>
<html lang="en">
<head>
<meta charset="utf-8">
<title>Saltmarsh Real Estate — Grand Opening Postcard</title>
<link rel="stylesheet" href="https://fonts.googleapis.com/css2?family=Montserrat:wght@600;700;800&display=swap">
<style>
  :root {
    --ocean: #0b7bbd;
    --ocean-text: #1a7fbe;
    --ink: #141414;
    --paper: #ffffff;
    --sky: #8fc3ea;
    --siding: #9fb8d2;
    --foliage: #6f7d4e;
    --mulch: #a77a52;
  }
  html, body {
    margin: 0;
    padding: 0;
    overflow: hidden;
    background: var(--paper);
  }
  .postcard {
    position: relative;
    width: 1200px;
    height: 768px;
    overflow: hidden;
    background: var(--paper);
    font-family: "Montserrat", Arial, sans-serif;
  }
  .shapes {
    position: absolute;
    inset: 0;
  }
  .headline {
    position: absolute;
    left: 20px;
    top: 14px;
    width: 700px;
    margin: 0;
    color: var(--ocean-text);
    font-size: 18.5px;
    font-weight: 700;
    line-height: 34px;
    text-transform: uppercase;
    white-space: nowrap;
  }
  .price-label {
    position: absolute;
    left: 23px;
    top: 150px;
    margin: 0;
    color: var(--paper);
    font-size: 28px;
    font-weight: 700;
    line-height: 1;
  }
  .price-range {
    position: absolute;
    left: 24px;
    top: 190px;
    margin: 0;
    color: var(--paper);
    font-size: 46px;
    font-weight: 800;
    line-height: 1;
  }
  .intro {
    position: absolute;
    left: 23px;
    top: 304px;
    width: 600px;
    margin: 0;
    color: var(--ink);
    font-size: 19.5px;
    font-weight: 700;
    line-height: 40px;
    white-space: nowrap;
  }
  .brand {
    position: absolute;
    left: 30px;
    top: 590px;
    width: 330px;
    text-align: center;
  }
  .brand-dot {
    display: block;
    width: 58px;
    height: 58px;
    margin: 0 auto 14px;
    border-radius: 50%;
    background: var(--ocean);
  }
  .brand-name {
    margin: 0;
    color: var(--ocean);
    font-size: 30px;
    font-weight: 700;
    letter-spacing: 3px;
    line-height: 1.25;
    text-transform: uppercase;
  }
  .appointment {
    position: absolute;
    left: 808px;
    top: 662px;
    width: 360px;
    color: var(--paper);
  }
  .appointment-label {
    margin: 0;
    font-size: 19px;
    font-weight: 700;
    line-height: 1;
  }
  .appointment-phone {
    display: block;
    margin-top: 12px;
    font-size: 44px;
    font-weight: 700;
    line-height: 1;
    color: var(--paper);
    text-decoration: none;
  }
</style>
</head>
<body>
  <main class="postcard">
    <svg class="shapes" width="1200" height="768" viewBox="0 0 1200 768">
      <defs>
        <linearGradient id="office-photo-tones" x1="0" y1="0" x2="0" y2="1">
          <stop offset="0" stop-color="#8fc3ea"/>
          <stop offset="0.18" stop-color="#a9b5bf"/>
          <stop offset="0.35" stop-color="#9fb8d2"/>
          <stop offset="0.72" stop-color="#8aa3bd"/>
          <stop offset="0.84" stop-color="#6f7d4e"/>
          <stop offset="1" stop-color="#a77a52"/>
        </linearGradient>
      </defs>
      <polygon class="office-photo" role="img"
        aria-label="Photo of the new light blue clapboard office building with shuttered windows, a small porch and landscaped trees"
        points="787,0 1200,0 1200,768 382,768" fill="url(#office-photo-tones)"/>
      <polygon class="price-band" points="0,125 721,125 649,262 0,262" fill="#0b7bbd"/>
      <polygon class="appointment-band" points="775,652 1200,652 1200,750 715,750" fill="#0b7bbd"/>
    </svg>

    <h1 class="headline">Grand opening April 7, 2016 at our new office.<br>Door prizes: Brindlecove Day Spa, Copper Kettle<br>Pies gift cards and a cruise giveaway.</h1>

    <p class="price-label">HOME PRICES BETWEEN</p>
    <p class="price-range">$300,000 - $2.2 MILLION</p>

    <p class="intro">We are an upscale, full service real estate boutique<br>based in Mt. Pleasant, SC.&nbsp; We will be having a<br>Grand Opening of our beautiful, new office<br>complete with high end custom home<br>architecture and design</p>

    <div class="brand">
      <span class="brand-dot"></span>
      <p class="brand-name">Saltmarsh<br>Real Estate</p>
    </div>

    <div class="appointment">
      <p class="appointment-label">SCHEDULE AN&nbsp; APPOINTMENT</p>
      <a class="appointment-phone" href="tel:8435550172">843-555-0172</a>
    </div>
  </main>
</body>
</html>
```